digger and truck hire

this is a new business - Digger and Truck
we would like to include the attached photo of the digger and truck - as the truck is red and the digger is green
maybe either black or white lettering which ever suits

Industry/Entity Type

Business

Contact Information for Business Card

RDL - Ruddas 2.5t Mini Digger and 7t Tip Truck -Hire, full attachments, augers, trenching, site preparation, small aggregate deliveries
Phone 0218365914
rudda.rdl@plinto.co.nz

```html
<!DOCTYPE html>
<html lang="en">
<head>
<meta charset="utf-8">
<title>RDL Business Card</title>
<link rel="stylesheet" href="https://fonts.googleapis.com/css2?family=Questrial&display=swap">
<style>
  :root {
    --orange: #e2481f;
    --orange-dark: #c23a16;
    --ink: #1a1a1a;
    --white: #ffffff;
    --page: #e9e9e9;
    --photo-sky: #eef1f3;
    --photo-steel: #c9d0d4;
    --photo-truck: #e9b9a4;
  }
  * { margin: 0; padding: 0; box-sizing: border-box; }
  html, body {
    width: 1200px; height: 1200px; overflow: hidden;
    background: var(--page);
    font-family: "Questrial", "Century Gothic", sans-serif;
    color: var(--ink);
  }
  .card {
    position: absolute; left: 60px; top: 291px;
    width: 1080px; height: 617px;
    background: var(--white);
    overflow: hidden;
    box-shadow: 0 4px 18px rgba(0,0,0,0.18);
  }
  .brand-name {
    position: absolute; left: 40px; top: 16px;
    font-size: 86px; line-height: 92px; letter-spacing: 2px;
    color: var(--orange);
  }
  .business-title {
    position: absolute; left: 296px; top: 72px;
    font-size: 31px; white-space: nowrap; letter-spacing: 0.3px;
  }
  .title-rule {
    position: absolute; left: 34px; right: 0; top: 113px;
    height: 6px; background: var(--orange);
  }
  .equipment-photo {
    position: absolute; left: 0; right: 0; top: 136px; bottom: 0;
    background:
      linear-gradient(180deg, rgba(255,255,255,0.35), rgba(255,255,255,0.2)),
      linear-gradient(100deg, var(--photo-truck) 0%, #f1e1d8 28%, var(--photo-steel) 55%, var(--photo-sky) 100%);
  }
  .service-list {
    position: absolute; left: 40px; top: 183px;
    list-style: none;
  }
  .service-list li {
    display: flex; align-items: center;
    font-size: 36px; line-height: 52px; white-space: nowrap;
  }
  .service-list li::before {
    content: ""; width: 14px; height: 14px; margin-right: 40px;
    background: var(--orange); border-radius: 50%;
  }
  .contact {
    position: absolute; left: 557px;
    display: flex; align-items: center; gap: 30px;
    font-size: 38px; white-space: nowrap;
  }
  .contact-phone { top: 176px; }
  .contact-email { top: 277px; }
  .contact svg { width: 60px; height: 60px; flex: none; }
  .footer-band {
    position: absolute; left: 0; bottom: 0;
    width: 1080px; height: 129px;
  }
  .footer-name {
    position: absolute; right: 27px; bottom: 14px;
    font-size: 100px; line-height: 100px; letter-spacing: 3px;
    color: var(--white);
  }
</style>
</head>
<body>
  <div class="card">
    <div class="equipment-photo" role="img" aria-label="Photo of the red tip truck carrying the green mini digger"></div>

    <div class="brand-name">RDL</div>
    <div class="business-title">RUDDAS 2.5T MINI DIGGER AND 7T TIP TRUCK-HIRE</div>
    <div class="title-rule"></div>

    <ul class="service-list">
      <li>Full Attachment</li>
      <li>Augers</li>
      <li>Trenching</li>
      <li>Site Preparation</li>
      <li>Small Aggregate Deliveries</li>
    </ul>

    <div class="contact contact-phone">
      <svg viewBox="0 0 60 60" aria-hidden="true">
        <circle cx="30" cy="30" r="27" fill="none" stroke="var(--orange)" stroke-width="4"/>
        <path d="M21 16c2-1 4 0 5 2l2 5c1 2 0 3-1 4l-2 2c1 4 5 8 9 9l2-2c1-1 2-2 4-1l5 2c2 1 3 3 2 5l-1 2c-2 3-6 3-10 1-6-3-12-9-15-15-2-4-2-8 0-10z" fill="var(--orange)"/>
      </svg>
      <span>0218365914</span>
    </div>
    <div class="contact contact-email">
      <svg viewBox="0 0 60 60" aria-hidden="true">
        <circle cx="30" cy="30" r="27" fill="none" stroke="var(--orange)" stroke-width="4"/>
        <rect x="15" y="20" width="30" height="20" fill="none" stroke="var(--orange)" stroke-width="3"/>
        <path d="M15 20l15 12 15-12M15 40l11-10M45 40l-11-10" fill="none" stroke="var(--orange)" stroke-width="3"/>
      </svg>
      <span>rudda.rdl@plinto.co.nz</span>
    </div>

    <svg class="footer-band" viewBox="0 0 1080 129" aria-hidden="true">
      <path d="M455 0H1080V129H0V72H388Z" fill="var(--orange)"/>
      <path d="M455 6H1080" stroke="var(--orange-dark)" stroke-width="2"/>
    </svg>
    <div class="footer-name">RDL</div>
  </div>
</body>
</html>
```